Brindle Deals is an online marketing platform

A daily deals site for consumers a way to bring in new clients for clients and this is who the business cards are for. Industries - Food and Drink, Things To Do, Beauty and Spas, Staycations and Services.This leaflet is going to be used to get member of the public to sign up to our website

```html
<!DOCTYPE html>
<html lang="en">
<head>
<meta charset="utf-8">
<title>Brindle Deals – Launch Leaflet</title>
<link href="https://fonts.googleapis.com/css2?family=Roboto:wght@400;500;700&family=Roboto+Condensed:wght@400&display=swap" rel="stylesheet">
<style>
  :root{
    --brand-blue:#1057a8;
    --stripe-grey:#96979b;
    --stripe-light:#d3d5d8;
    --paper-top:#f5f6f7;
    --paper-edge:#e3e5e8;
    --body-grey:#444649;
    --label-grey:#4a4c50;
    --page-bg:#e9ecef;
    --white:#ffffff;
    --dash-grey:#8d9094;
  }
  *{margin:0;padding:0;box-sizing:border-box;}
  html,body{width:1200px;height:1200px;overflow:hidden;background:var(--page-bg);}
  body{position:relative;font-family:'Roboto',Arial,sans-serif;}

  .leaflet{
    position:absolute;left:190px;top:20px;width:950px;height:1344px;
    transform:scale(0.863);transform-origin:top left;
    background:radial-gradient(ellipse at 50% 35%,var(--white) 0%,var(--paper-top) 40%,var(--paper-edge) 100%);
    overflow:hidden;
  }
  .leaflet__shapes{position:absolute;left:0;top:0;}
  .leaflet__form-area{position:absolute;left:0;top:995px;width:950px;height:349px;background:var(--white);}

  .centered{position:absolute;left:0;width:950px;text-align:center;}

  .brand-name{top:88px;display:flex;justify-content:center;align-items:center;gap:18px;
    font-size:70px;font-weight:700;color:var(--brand-blue);letter-spacing:-1px;}
  .brand-name__dot{width:46px;height:46px;border-radius:50%;background:var(--brand-blue);}

  .headline{top:262px;font-size:104px;font-weight:700;color:var(--brand-blue);letter-spacing:-2px;}
  .prize{top:380px;font-size:39px;color:var(--brand-blue);}
  .prize-sub{top:429px;font-size:29px;color:var(--brand-blue);}
  .intro{top:476px;font-size:18px;line-height:23px;color:var(--body-grey);}

  .category{position:absolute;top:563px;width:150px;margin-left:-75px;text-align:center;}
  .category__label{display:block;margin-top:2px;font-size:12px;color:var(--label-grey);}

  .launch-icon{position:absolute;left:452px;top:684px;}
  .launch-title{top:738px;font-size:29px;font-weight:700;color:var(--white);}
  .launch-sub{top:776px;font-size:29px;color:var(--white);}
  .register{top:830px;font-size:20px;color:var(--white);}
  .register__site{font-size:27px;font-weight:700;}
  .register-cta{top:863px;font-size:29px;font-weight:700;color:var(--white);}
  .follow{top:910px;font-size:18px;color:var(--white);}
  .social{top:941px;display:flex;justify-content:center;gap:20px;}
  .social__dot{width:38px;height:38px;border-radius:50%;background:var(--white);}

  .form-intro{position:absolute;left:91px;top:1027px;width:800px;font-size:18px;line-height:23px;color:var(--brand-blue);}
  .form-row{position:absolute;left:200px;width:620px;display:flex;align-items:flex-end;}
  .form-row__label{width:90px;font-size:20px;font-weight:700;color:var(--brand-blue);}
  .form-row__line{flex:1;height:14px;border-bottom:2px dashed var(--brand-blue);margin-left:0;}
  .opt-out{position:absolute;left:82px;top:1287px;font-family:'Roboto Condensed',Arial,sans-serif;font-size:19px;color:var(--brand-blue);}
</style>
</head>
<body>
<main class="leaflet">
  <svg class="leaflet__shapes" width="950" height="1344" viewBox="0 0 950 1344" aria-hidden="true">
    <!-- left stripes -->
    <polygon points="0,220 222,0 236,0 0,312" fill="var(--stripe-grey)"/>
    <polygon points="232,0 242,0 0,458 0,368" fill="var(--brand-blue)"/>
    <polygon points="242,0 248,0 40,560 8,545" fill="var(--stripe-light)"/>
    <!-- right stripes -->
    <polygon points="950,220 728,0 714,0 950,312" fill="var(--stripe-grey)"/>
    <polygon points="718,0 708,0 950,458 950,368" fill="var(--brand-blue)"/>
    <polygon points="708,0 702,0 910,560 942,545" fill="var(--stripe-light)"/>
    <!-- central blue band -->
    <polygon points="0,540 145,670 790,670 950,540 950,872 805,995 130,995 0,866" fill="var(--brand-blue)"/>
    <line x1="0" y1="995" x2="950" y2="995" stroke="var(--dash-grey)" stroke-width="1.5" stroke-dasharray="9 7"/>
  </svg>
  <div class="leaflet__form-area"></div>

  <div class="centered brand-name"><span class="brand-name__dot"></span>Brindle Deals</div>

  <h1 class="centered headline">Hey You!</h1>
  <p class="centered prize">Want to win £200 to spend</p>
  <p class="centered prize-sub">on the best experiences the South West has to offer?</p>
  <p class="centered intro">Brindle Deals is a brand spanking new website that gives you access to<br>exciting offers across the best restaurants, hotels, spas, leisure activities and services.<br>Pretty cool?</p>

  <div class="category" style="left:212px"><svg width="54" height="66" viewBox="0 0 54 66"><path d="M27 3a23 23 0 0 1 23 23c0 14-23 34-23 34S4 40 4 26A23 23 0 0 1 27 3z" fill="none" stroke="var(--brand-blue)" stroke-width="2"/><circle cx="27" cy="26" r="15" fill="none" stroke="var(--brand-blue)" stroke-width="1.5"/><rect x="19" y="19" width="16" height="14" fill="var(--brand-blue)"/><ellipse cx="27" cy="62" rx="24" ry="3" fill="none" stroke="var(--brand-blue)" stroke-width="1.5"/></svg><span class="category__label">RESTAURANTS</span></div>
  <div class="category" style="left:343px"><svg width="54" height="66" viewBox="0 0 54 66"><path d="M27 3a23 23 0 0 1 23 23c0 14-23 34-23 34S4 40 4 26A23 23 0 0 1 27 3z" fill="none" stroke="var(--brand-blue)" stroke-width="2"/><circle cx="27" cy="26" r="15" fill="none" stroke="var(--brand-blue)" stroke-width="1.5"/><path d="M22 17v18M19 17v6h6v-6M32 17v18M32 17c3 1 3 8 0 9" fill="none" stroke="var(--brand-blue)" stroke-width="2"/><ellipse cx="27" cy="62" rx="24" ry="3" fill="none" stroke="var(--brand-blue)" stroke-width="1.5"/></svg><span class="category__label">HOTELS</span></div>
  <div class="category" style="left:474px"><svg width="54" height="66" viewBox="0 0 54 66"><path d="M27 3a23 23 0 0 1 23 23c0 14-23 34-23 34S4 40 4 26A23 23 0 0 1 27 3z" fill="none" stroke="var(--brand-blue)" stroke-width="2"/><circle cx="27" cy="26" r="15" fill="none" stroke="var(--brand-blue)" stroke-width="1.5"/><path d="M27 17c4 4 4 10 0 15c-4-5-4-11 0-15zM18 24c5 0 9 4 9 8c-5 0-9-3-9-8zM36 24c-5 0-9 4-9 8c5 0 9-3 9-8z" fill="none" stroke="var(--brand-blue)" stroke-width="1.5"/><ellipse cx="27" cy="62" rx="24" ry="3" fill="none" stroke="var(--brand-blue)" stroke-width="1.5"/></svg><span class="category__label">SPAS</span></div>
  <div class="category" style="left:602px"><svg width="54" height="66" viewBox="0 0 54 66"><path d="M27 3a23 23 0 0 1 23 23c0 14-23 34-23 34S4 40 4 26A23 23 0 0 1 27 3z" fill="none" stroke="var(--brand-blue)" stroke-width="2"/><circle cx="27" cy="26" r="15" fill="none" stroke="var(--brand-blue)" stroke-width="1.5"/><path d="M16 26q3-3 6 0t6 0t6 0t5 0M16 31q3-3 6 0t6 0t6 0t5 0" fill="none" stroke="var(--brand-blue)" stroke-width="2"/><ellipse cx="27" cy="62" rx="24" ry="3" fill="none" stroke="var(--brand-blue)" stroke-width="1.5"/></svg><span class="category__label">LEISURE ACTIVITIES</span></div>
  <div class="category" style="left:736px"><svg width="54" height="66" viewBox="0 0 54 66"><path d="M27 3a23 23 0 0 1 23 23c0 14-23 34-23 34S4 40 4 26A23 23 0 0 1 27 3z" fill="none" stroke="var(--brand-blue)" stroke-width="2"/><circle cx="27" cy="26" r="15" fill="none" stroke="var(--brand-blue)" stroke-width="1.5"/><circle cx="27" cy="26" r="7" fill="none" stroke="var(--brand-blue)" stroke-width="4" stroke-dasharray="3 2"/><circle cx="27" cy="26" r="2.5" fill="var(--brand-blue)"/><ellipse cx="27" cy="62" rx="24" ry="3" fill="none" stroke="var(--brand-blue)" stroke-width="1.5"/></svg><span class="category__label">SERVICES</span></div>

  <svg class="launch-icon" width="46" height="50" viewBox="0 0 46 50" aria-hidden="true"><rect x="2" y="14" width="42" height="26" rx="3" fill="var(--white)"/><rect x="19" y="40" width="8" height="6" fill="var(--white)"/><rect x="12" y="46" width="22" height="3" fill="var(--white)"/><path d="M23 2c5 5 5 13 2 18h-4c-3-5-3-13 2-18z" fill="var(--white)" stroke="var(--brand-blue)" stroke-width="2"/></svg>

  <p class="centered launch-title">Launching on the 1st August 2019</p>
  <p class="centered launch-sub">Be the first to receive exclusive offers and WIN!</p>
  <p class="centered register">Register for free now at <span class="register__site">brindledeals.co.uk</span> and find inspiration for places to</p>
  <p class="centered register-cta">EAT, things to DO and where to get a PAMPER.</p>
  <p class="centered follow">Follow us on</p>
  <div class="centered social"><span class="social__dot"></span><span class="social__dot"></span><span class="social__dot"></span></div>

  <p class="form-intro">Complete your details below for your chance to win and be the first to receive fresh fancy offers just for you.</p>
  <div class="form-row" style="top:1094px"><span class="form-row__label">Name:</span><span class="form-row__line"></span></div>
  <div class="form-row" style="top:1143px"><span class="form-row__label">Email:</span><span class="form-row__line"></span></div>
  <div class="form-row" style="top:1193px"><span class="form-row__label">Mobile:</span><span class="form-row__line"></span></div>
  <div class="form-row" style="top:1243px"><span class="form-row__label">Address:</span><span class="form-row__line"></span></div>
  <p class="opt-out">[&nbsp;&nbsp;&nbsp;] Please tick here if you would not like to receive updates on fabulous offers and new experiences.</p>
</main>
</body>
</html>
```